Beauty Salon Industry - Web Design Project

zQuarta is a well-funded start up developing an Online Marketing Platform for small businesses in Europe.
We require a large number of high quality business web designs for our business website builder. Our business websites are seamlessly integrated into our Online Marketing systems and therefore it is important for designers to comply with our Design Guidelines.
This is our second contest and it will focus on the beauty salon industry. We will be running contents every 2-3 weeks for a new industry. Last month, we ran a contest for Builder website designs with 3 top prizes (plus £10 per variation) and we also paid out £25 per design for 20+ entries from designers who did not win the top prizes. So we encourage all entries!
We have included a wire frame this time to encourage you to be as creative as possible with your designs and layout while respecting the following guidelines:
1) You CAN change the layout as much as you like. If you think a vertical menu would look better, then use it. If you think the design would benefit from moving an element to a different location, then you can do that too.
2) You must include ALL the elements in the wire frame in your design.(e.g. latest 2 news entries, a testimonial, 1 gallery image, carousel etc...). Please make sure you have looked through the wire frame and know what is required. Entries that do not include all the elements will not qualify to win.
3) So remember, you CAN change the layout as much as you like but DO NOT remove any elements nor move them to a different page.
4) You may change the size and style of the carousel image. We would like to see as many variations of this as possible.
We are rewarding 3 prizes, and would like the winning designer to design the internal pages to the new design.
As always, if we think your designs could be incorporated into our system, but you do not win the competition, we will reward £25. Therefore, we encourage designers to submit as many designs as possible as we may award up to 25 designs.
Judging criteria : -
1) Visual Design
2) Layout must adhere to best practices and wireframe. If you decide to move elements around significantly please provide reason
3) Functional, informative and drives calls to action
Updates
As usual:
1st place = £350
2nd place = £250
3rd place = £150
Good luck!
Very happy with all the designs submitted so far, and will provide feedback ASAP.
We would like to see you try arranging the elements differently. So please try different navigation types and layouts.
Thanks
Morris
Prize funds for 1st place has been slightly increased.
Thanks
Morris
We have already had some amazing designs submitted. Thanks.
Remember to play with the layout of the elements and try designs with a carousel/slider that is in portrait not just in landscape.
Thanks everyone!
Morris
Hi everyone, we are really enjoying looking through the designs.
We have one NEW requirement. If you have used an image from http://www.frelik-example.com/ in your design, could you please replace it with another.
We are not associated with them.
Thank you.
I have just sent a poll around the office to vote on all the designs and hope to have the results soon.
Good luck and I hope to see all your great designs for our next project in a couple of weeks.
Morris
Hi everyone, we hope you have had a good holiday season. We will be rewarding the prizes very soon, hopefully today or tomorrow.
Thanks
Morris
We are currently going through all the designs that did not win our competition and will be contacting the designers of the designs we would like to use in our system, so please keep an eye on your inbox over the next few days.
Thank you
Morris
Target Market(s)
Beauty Salon Industry
Industry/Entity Type
Beauty Salon
Look and feel
Each slider illustrates characteristics of the customer's brand and the style your logo design should communicate.

```html
<!DOCTYPE html>
<html lang="en">
<head>
<meta charset="utf-8">
<title>Lushcut – Hair and Urban Spa</title>
<link rel="stylesheet" href="https://fonts.googleapis.com/css2?family=Cinzel:wght@400;700&family=Noto+Serif:ital,wght@0,400;1,400&family=Open+Sans:wght@400;600&display=swap">
<style>
  :root{
    --pink:#e8418c;
    --pink-soft:#f06aa7;
    --pink-light:#f7b6d3;
    --ink:#222;
    --text:#444;
    --muted:#888;
    --side:#f1f1f1;
    --side-line:#dedede;
    --rule:#e4e4e4;
    --strip:#efefef;
    --orange:#f2741c;
  }
  *{box-sizing:border-box;margin:0;padding:0}
  html,body{width:959px;height:1200px;overflow:hidden;background:#fff}
  body{position:relative;font-family:"Noto Serif",Georgia,serif;color:var(--text)}
  .abs{position:absolute}

  /* sidebar */
  .sidebar{left:0;top:0;width:275px;height:1200px;background:linear-gradient(90deg,#f6f6f6,#ececec);border-right:1px solid var(--side-line)}
  .brand{left:64px;top:22px;display:flex;align-items:center;gap:10px}
  .brand-dot{width:40px;height:40px;border-radius:50%;background:var(--pink)}
  .brand-name{font-family:"Noto Serif",serif;font-size:34px;color:var(--pink);letter-spacing:1px}
  .brand-tag{left:114px;top:70px;font-family:"Cinzel",serif;font-size:11px;color:#333;letter-spacing:1px}
  .nav{left:0;top:106px;width:273px;list-style:none}
  .nav li{height:39.5px;line-height:39.5px;text-align:right;padding-right:26px;font-size:15px;color:#333;letter-spacing:.5px}
  .nav li.is-active{margin-left:56px;background:linear-gradient(#f27db3,var(--pink));color:#fff;border-top:1px dashed #fbc6dd;border-bottom:1px dashed #fbc6dd;box-shadow:0 2px 3px rgba(0,0,0,.15)}
  .nav li.is-current{color:var(--pink-soft);background:linear-gradient(90deg,rgba(0,0,0,0),#e2e2e2)}
  .side-rule{left:0;width:275px;height:1px;background:var(--side-line)}
  .gallery-thumb{left:61px;top:427px;width:188px;height:127px;border:4px solid #fff;box-shadow:0 1px 4px rgba(0,0,0,.2);background:linear-gradient(135deg,#5a4a3e,#d9b48f 55%,#7c6a5a)}
  .link-caps{font-family:"Cinzel",serif;font-size:12px;color:var(--pink);letter-spacing:1px}
  .quote{left:48px;top:610px;width:190px;font-style:italic;font-size:13px;line-height:20px;color:#333}
  .quote a{color:var(--pink);text-decoration:none}
  .quote-by{left:48px;top:702px;font-family:"Cinzel",serif;font-size:12px;color:#444;letter-spacing:1px;line-height:17px}
  .quote-by small{font-size:10px}

  /* header */
  .call{left:571px;top:8px;font-size:24px;color:var(--pink-soft)}
  .call span{color:#333}
  .book-now{left:812px;top:0;width:108px;height:46px;background:linear-gradient(#f68bbd,var(--pink));color:#fff;font-family:"Open Sans",sans-serif;font-weight:600;font-size:16px;text-align:center;line-height:42px;border-bottom:2px dashed #fff;box-shadow:0 2px 3px rgba(0,0,0,.2)}

  /* slider */
  .slider{left:312px;top:78px;width:614px;height:278px;border:2px solid var(--pink-light)}
  .slide{position:absolute;inset:3px;background:linear-gradient(160deg,#f3efe8 0%,#c9a27a 40%,#7a4e2e 65%,#3a3a3a 100%)}
  .slide-arrow{position:absolute;top:128px;width:30px;height:30px;background:#fff;display:flex;align-items:center;justify-content:center}
  .slide-arrow.prev{left:0}
  .slide-arrow.next{right:0}
  .dots{left:610px;top:378px;display:flex;gap:7px}
  .dots i{width:8px;height:8px;border-radius:50%;background:#ddd;display:block}
  .dots i.on{background:#333}
  .dots-line{left:520px;top:382px;width:330px;height:1px;background:linear-gradient(90deg,transparent,#ddd,transparent)}

  /* intro */
  .intro-icon{left:314px;top:407px;width:30px;height:30px;border-radius:50%;background:var(--pink-soft)}
  .intro-title{left:354px;top:410px;font-size:19px;color:var(--pink-soft)}
  .intro-text{left:317px;top:440px;width:612px;font-size:13px;line-height:20px;color:#333}
  .intro-text .more{font-family:"Cinzel",serif;font-size:12px;color:var(--pink)}

  /* news */
  .news-heading{left:316px;top:541px;font-family:"Cinzel",serif;font-size:18px;color:#111;font-weight:700}
  .view-all{left:618px;top:540px;width:103px;height:26px;background:linear-gradient(#f27db3,var(--pink));color:#fff;font-family:"Cinzel",serif;font-size:12px;text-align:center;line-height:26px;box-shadow:0 2px 2px rgba(0,0,0,.15)}
  .news-item{left:316px;width:406px;height:150px}
  .news-title{font-family:"Cinzel",serif;font-size:15px;color:var(--pink)}
  .news-photo{position:absolute;left:0;top:24px;width:125px;height:86px;background:linear-gradient(120deg,#cfcfcf,#8a6a55 55%,#e9e3dd)}
  .news-body{position:absolute;left:140px;top:20px;width:265px;font-family:"Open Sans",sans-serif}
  .news-date{font-size:9px;color:var(--muted)}
  .news-text{font-size:10.5px;line-height:16px;color:#444;margin-top:3px}
  .read-more{display:inline-block;margin-top:6px;width:88px;height:22px;line-height:22px;padding-left:12px;font-size:11px;color:#333;background:linear-gradient(90deg,#e6e6e6,#f7f7f7);clip-path:polygon(0 0,88% 0,100% 50%,88% 100%,0 100%)}
  .news-rule{position:absolute;left:0;top:148px;width:406px;height:1px;background:linear-gradient(90deg,transparent,var(--rule),transparent)}

  /* right column */
  .promo{left:747px;top:529px;width:181px;height:191px;background:linear-gradient(#fff,#f1f1f1);box-shadow:0 1px 3px rgba(0,0,0,.12)}
  .promo-product{position:absolute;left:32px;top:16px;width:110px;height:95px;background:radial-gradient(ellipse at 45% 40%,#555,#1c1c1c 60%,transparent 62%)}
  .promo-text{position:absolute;left:0;top:118px;width:181px;text-align:center;font-family:"Open Sans",sans-serif;font-size:11px;line-height:15px;color:#222}
  .promo-btn{position:absolute;left:0;bottom:0;width:181px;height:34px;line-height:34px;text-align:center;background:linear-gradient(#f27db3,var(--pink));color:#fff;font-family:"Cinzel",serif;font-size:13px;border-top:1px dashed #fbc6dd}
  .badge{left:897px;top:516px;width:48px;height:48px;border-radius:50%;background:radial-gradient(circle at 40% 35%,#ff9b3d,var(--orange));border:2px solid #fff;box-shadow:0 1px 3px rgba(0,0,0,.3);color:#fff;font-family:"Open Sans",sans-serif;font-weight:600;font-size:18px;text-align:center;line-height:44px}
  .info-title{left:747px;font-family:"Cinzel",serif;font-size:14px;color:#111;font-weight:700;display:flex;align-items:center;gap:8px}
  .info-text{left:751px;font-family:"Open Sans",sans-serif;font-size:10.5px;line-height:19px;color:#333}
  .hours{list-style:none;font-size:10px;line-height:17px}

  /* partners + footer */
  .partners{left:313px;top:1025px;width:615px;height:67px;background:linear-gradient(#f5f5f5,#ebebeb);display:flex;justify-content:space-around;align-items:center;padding:0 40px}
  .partner{background:#cfcfcf;height:14px;border-radius:2px}
  .footer{left:313px;top:1107px;width:615px;height:28px;background:var(--strip);font-family:"Open Sans",sans-serif;font-size:10px;color:#666;display:flex;justify-content:space-between;align-items:center;padding:0 14px}
</style>
</head>
<body>

<aside class="sidebar abs" aria-label="Site sidebar"></aside>

<div class="brand abs"><span class="brand-dot"></span><span class="brand-name">Lushcut</span></div>
<div class="brand-tag abs">Hair and Urban Spa</div>

<ul class="nav abs">
  <li class="is-active">Home</li>
  <li>Services</li>
  <li class="is-current">Gallery</li>
  <li>Testimonials</li>
  <li>News</li>
  <li>About Us</li>
  <li>Contact Us</li>
</ul>

<div class="side-rule abs" style="top:404px"></div>
<div class="gallery-thumb abs" role="img" aria-label="Gallery photo: stylist with a smiling client"></div>
<div class="link-caps abs" style="left:137px;top:562px">:: View Gallery</div>
<div class="side-rule abs" style="top:592px"></div>

<p class="quote abs">"My hairstylist, Nadia, was truly amazing. She listened to exactly what I wanted, but also <a href="#">more...</a></p>
<p class="quote-by abs">- Mara Ellison<br><small>USA California</small></p>

<div class="call abs">Call: <span>020 7946 0815</span></div>
<div class="book-now abs">BOOK NOW</div>

<div class="slider abs">
  <div class="slide" role="img" aria-label="Carousel photo: salon interior with styling chairs and mirrors"></div>
  <div class="slide-arrow prev"><svg width="12" height="14" viewBox="0 0 12 14"><path d="M9 1 3 7l6 6" fill="none" stroke="#222" stroke-width="2.5"/></svg></div>
  <div class="slide-arrow next"><svg width="12" height="14" viewBox="0 0 12 14"><path d="M3 1l6 6-6 6" fill="none" stroke="#222" stroke-width="2.5"/></svg></div>
</div>
<div class="dots-line abs"></div>
<div class="dots abs"><i class="on"></i><i></i><i></i></div>

<div class="intro-icon abs"></div>
<h1 class="intro-title abs" style="font-weight:400">Let Our Hair and Beauty Skills Blow You Away</h1>
<p class="intro-text abs">Lushcut is a passionate, creative team, dedicated to delivering a second to none, personal salon experience that will 'blow' your mind. Lushcut is a passionate, creative team, dedicated to delivering a second to none, personal salon experience that will 'blow' your mind. <span class="more">:: More</span></p>

<h2 class="news-heading abs">Latest News</h2>
<div class="view-all abs">:: View all</div>

<article class="news-item abs" style="top:578px">
  <h3 class="news-title" style="font-weight:400">Book Now for Christmas</h3>
  <div class="news-photo" role="img" aria-label="News photo: client having hair blow-dried"></div>
  <div class="news-body">
    <div class="news-date">31st December 2011</div>
    <p class="news-text">Our salon is usually very busy for the two weeks before Christmas, so please boomas, so please book early</p>
    <span class="read-more">Read more</span>
  </div>
  <div class="news-rule"></div>
</article>
<article class="news-item abs" style="top:732px">
  <h3 class="news-title" style="font-weight:400">Want to be a hair model?</h3>
  <div class="news-photo" role="img" aria-label="News photo: client having hair blow-dried"></div>
  <div class="news-body">
    <div class="news-date">31st December 2011</div>
    <p class="news-text">Our salon is usually very busy for the two weeks before Christmas, so please boomas, so please book early</p>
    <span class="read-more">Read more</span>
  </div>
  <div class="news-rule"></div>
</article>
<article class="news-item abs" style="top:885px">
  <h3 class="news-title" style="font-weight:400">Want to be a hair model?</h3>
  <div class="news-photo" role="img" aria-label="News photo: client having hair blow-dried"></div>
  <div class="news-body">
    <div class="news-date">31st December 2011</div>
    <p class="news-text">Our salon is usually very busy for the two weeks before Christmas, so please boomas, so please book early</p>
    <span class="read-more">Read more</span>
  </div>
</article>

<div class="promo abs">
  <div class="promo-product" role="img" aria-label="Product photo: hair dryer"></div>
  <p class="promo-text">Complimentary gift for first-<br>time clients!</p>
  <div class="promo-btn">Book appointment</div>
</div>
<div class="badge abs">£25</div>

<h4 class="info-title abs" style="top:740px">
  <svg width="10" height="14" viewBox="0 0 10 14"><path d="M5 0a5 5 0 0 0-5 5c0 4 5 9 5 9s5-5 5-9a5 5 0 0 0-5-5z" fill="var(--pink)"/><circle cx="5" cy="5" r="2" fill="#fff"/></svg>
  Our Address
</h4>
<p class="info-text abs" style="top:766px">12 Mercer Row<br>London W1X 2AB</p>

<h4 class="info-title abs" style="top:827px">
  <svg width="13" height="13" viewBox="0 0 13 13"><circle cx="6.5" cy="6.5" r="5.5" fill="none" stroke="var(--pink)" stroke-width="1.6"/><path d="M6.5 3.5v3.3l2.2 1.4" fill="none" stroke="var(--pink)" stroke-width="1.4"/></svg>
  Business Hours
</h4>
<ul class="info-text hours abs" style="top:852px">
  <li>Mon. 9 a.m - 5 p.m</li>
  <li>Tue. 9 a.m - 5 p.m</li>
  <li>Wed. 9 a.m - 5 p.m</li>
  <li>Thu. 9 a.m - 5 p.m</li>
  <li>Fri. 9 a.m - 5 p.m</li>
  <li>Sat. 9 a.m - 5 p.m</li>
</ul>

<div class="partners abs" aria-label="Partner brands">
  <span class="partner" style="width:86px"></span>
  <span class="partner" style="width:46px;height:28px"></span>
  <span class="partner" style="width:46px;height:30px"></span>
  <span class="partner" style="width:68px"></span>
</div>

<footer class="footer abs">
  <span>©2011 Lushcut.com All rights reserved</span>
  <span>Managed by Northlane Studio | Admin</span>
</footer>

</body>
</html>
```